Business Cards for Demolition & Salvage Company

We are Licensed Demolition Contractors and this business card design is for our Salvage Yard. We recycle over 95% of the building materials removed from each demolition site in which we take to our Salvage Yard for resale eg. bricks, windows, doors, kitchens, stoves, lights, fencing etc so pretty much everything.
Updates

I forgot to note that single sided business card only please.

Project Deadline Extended
Reason: I would like to ask if designers could please submit or re-submit their designs edited to a single sided card only. The card also does not need space for an employee name or position as our general business contact details will suffice for this project. Primary colour must be ROYAL BLUE with no exceptions please. Much appreciated and thank you to all whom have submitted designs to date and I look forward to receiving your edited designs..

Industry/Entity Type

Building

Contact Information for Business Card

Fendrell Demolition & Salvage (WA) Pty Ltd
2437 Old Quarry Parade
UPPER MARLOW WA 6071
P: (08) 9471 3058
F: (08) 9471 2267
E: salvage@fdwreck.com.au
W: fendrelldemolition.com.au

Requirements
Must have
• We have a logo that has been with our Company since 1974 so he must be included in the design - file attached. As for colours, we have always used royal blue and again this must be the primary colour used in the design. Please keep the design simple.
Nice to have
• Card can include opening hours as follows:
Opening Hours:
Monday to Friday 8am - 5.00pm
Saturday 8am - 3pm
Closed Sunday's and public holidays

```html
<!DOCTYPE html>
<html lang="en">
<head>
<meta charset="utf-8">
<title>Fendrell Demolition &amp; Salvage – Business Card</title>
<link href="https://fonts.googleapis.com/css2?family=Cabin:wght@400;700&display=swap" rel="stylesheet">
<style>
  :root {
    --royal-blue: #24368e;
    --ink: #1b1b1b;
    --paper: #ffffff;
    --shadow-grey: #c4c4c8;
  }
  * { margin: 0; padding: 0; box-sizing: border-box; }
  html, body { width: 1200px; height: 741px; overflow: hidden; background: var(--paper); }
  .card {
    position: relative;
    width: 1200px;
    height: 741px;
    background: var(--paper);
    font-family: "Cabin", "Gill Sans", sans-serif;
    color: var(--ink);
  }
  .contact {
    position: absolute;
    left: 43px;
    top: 36px;
    font-size: 28px;
    line-height: 50px;
  }
  .contact .company-name {
    font-weight: 700;
    font-size: 30px;
    line-height: 40px;
    margin-bottom: 2px;
  }
  .contact .label { font-weight: 700; display: inline-block; width: 38px; }
  .brand-mark {
    position: absolute;
    left: 865px;
    top: 200px;
    width: 240px;
    display: flex;
    align-items: center;
    gap: 12px;
    font-weight: 700;
    font-size: 34px;
    color: var(--royal-blue);
  }
  .brand-mark .mark-square {
    width: 26px; height: 26px; background: var(--royal-blue);
  }
  .hours-tag {
    position: absolute;
    left: 863px;
    top: 306px;
    width: 296px;
    height: 76px;
    background: var(--royal-blue);
    box-shadow: 6px 6px 0 var(--shadow-grey);
    color: var(--paper);
    font-weight: 700;
    font-size: 32px;
    display: flex;
    align-items: center;
    justify-content: center;
  }
  .hours {
    position: absolute;
    right: 45px;
    top: 395px;
    text-align: right;
    font-size: 30px;
    line-height: 50px;
  }
  .brick-band {
    position: absolute;
    left: 0;
    top: 549px;
    width: 1200px;
    height: 192px;
    background: linear-gradient(180deg, var(--royal-blue), #2f44a3);
  }
</style>
</head>
<body>
  <div class="card">
    <div class="contact">
      <div class="company-name">Fendrell Demolition &amp; Salvage (WA) Pty Ltd</div>
      <div>2437 Old Quarry Parade, UPPER MARLOW, WA, 6071</div>
      <div><span class="label">P</span>(08) 9471 3058</div>
      <div><span class="label">F</span>(08) 9471 2267</div>
      <div><span class="label">E</span>salvage@fdwreck.com.au</div>
      <div>www.fendrelldemolition.com.au</div>
    </div>

    <div class="brand-mark">
      <span class="mark-square"></span>
      <span>Fendrell</span>
    </div>

    <div class="hours-tag">Opening Hours</div>

    <div class="hours">
      <div>Monday to Friday 8am - 5.00pm</div>
      <div>Saturday 8am - 3pm</div>
      <div>Closed Sundays &amp; Public holidays</div>
    </div>

    <div class="brick-band" role="img" aria-label="Royal blue brick wall pattern along the bottom edge"></div>
  </div>
</body>
</html>
```